Professional law firm looking for new professional and eye-catching business card design

Law firm in need of new business card design using existing firm logo and firm colors on thick card stock. Firm colors are navy blue, cyan blue, and gray. Please use firm's logo either on the back of the card or on the front and back. I am looking for something eye-catching and resonating but also professional.

Target Market(s)

Law firm growth by attracting clients with professional, creative, and attractive business cards.

Industry/Entity Type

Legal/Law Firm

Contact Information for Business Card

Name: Derek T. Halloway, Esq., Address: 517 E. Quintley Blvd., P.O. Box 641, Tavares, FL 32790, Phone numbers: (352) 555-0187 Office, (352) 555-0142 Fax, email address: DerekH@hqlegalfx.com, website: www.HQLegalFX.com

Font styles to use
Other font styles liked:
• Font as close as possible to matching law firm logo.

Requirements
Must have
• Must have business card details and law firm logo with law firm colors.

```html
<!DOCTYPE html>
<html lang="en">
<head>
<meta charset="utf-8">
<title>HQ Legal, P.A. – Business Card</title>
<link rel="stylesheet" href="https://fonts.googleapis.com/css2?family=Della+Respira&family=Alike&display=swap">
<style>
  :root {
    --navy: #06083a;
    --cyan: #1aa7e6;
    --grey: #b3b1b5;
    --ink: #0b0d45;
    --paper: #ffffff;
    --card-w: 394px;
    --card-h: 226px;
  }
  * { margin: 0; padding: 0; box-sizing: border-box; }
  html, body {
    width: 1200px; height: 900px; overflow: hidden;
    background: var(--paper);
    font-family: "Della Respira", "Alike", serif;
  }
  .canvas { position: relative; width: 1200px; height: 900px; }

  .card {
    position: absolute;
    top: 337px;
    width: var(--card-w);
    height: var(--card-h);
    overflow: hidden;
  }

  /* Front */
  .card-front { left: 208px; background: var(--navy); }
  .card-front .edge-tab {
    position: absolute; right: 0; top: 18px;
    width: 23px; height: 58px; background: var(--grey);
  }
  .firm-mark {
    position: absolute; left: 0; right: 0; top: 50%;
    transform: translateY(-50%);
    display: flex; align-items: center; justify-content: center; gap: 14px;
    color: var(--cyan);
    font-family: "Della Respira", "Alike", serif;
    font-weight: 400;
    font-size: 32px; letter-spacing: 1.5px;
    white-space: nowrap;
  }
  .firm-mark .mark-square {
    width: 30px; height: 30px; background: var(--grey); flex: none;
  }

  /* Back */
  .card-back { left: 631px; background: var(--grey); color: var(--ink); }
  .card-back .brand-band {
    position: absolute; left: 0; right: 0; top: 18px; height: 58px;
    background: var(--navy);
    display: flex; align-items: center; justify-content: center;
  }
  .brand-band .firm-name-small {
    color: var(--cyan); font-size: 12px; letter-spacing: 0.8px;
  }
  .attorney-name {
    position: absolute; left: 0; right: 0; top: 83px;
    text-align: center; font-size: 18px; font-weight: 400; letter-spacing: 0.3px;
  }
  .address {
    position: absolute; left: 0; right: 0; top: 111px;
    text-align: center; font-size: 10.5px; line-height: 13.6px;
  }
  .contact-row {
    position: absolute; left: 0; right: 0;
    font-size: 10.5px; height: 14px; line-height: 14px;
  }
  .contact-row span { position: absolute; white-space: nowrap; }
  .row-1 { top: 163px; }
  .row-2 { top: 177px; }
  .label-left  { left: 71px; }
  .value-left  { left: 96px; }
  .label-right { left: 195px; }
  .value-right { left: 221px; }
</style>
</head>
<body>
<main class="canvas">

  <section class="card card-front" aria-label="Card front">
    <div class="edge-tab"></div>
    <div class="firm-mark">
      <span class="mark-square"></span>
      <span class="firm-name">HQ Legal, P.A.</span>
    </div>
  </section>

  <section class="card card-back" aria-label="Card back">
    <div class="brand-band">
      <span class="firm-name-small">HQ Legal, P.A.</span>
    </div>
    <h1 class="attorney-name">Derek T. Halloway, Esq.</h1>
    <p class="address">
      517 E. Quintley Blvd.<br>
      P.O. Box 641<br>
      Tavares, FL 32790
    </p>
    <div class="contact-row row-1">
      <span class="label-left">P</span>
      <span class="value-left">: (352) 555-0187</span>
      <span class="label-right">E</span>
      <span class="value-right">: DerekH@hqlegalfx.com</span>
    </div>
    <div class="contact-row row-2">
      <span class="label-left">Fx</span>
      <span class="value-left">: (352) 555-0142</span>
      <span class="label-right">Web</span>
      <span class="value-right">: www.HQLegalFX.com</span>
    </div>
  </section>

</main>
</body>
</html>
```